Women's Health Company needs business card

We need a business card for a USA based women's health care company. We use digital technology to enhance therapy prescribed by clinicians for their patients

```html
<!DOCTYPE html>
<html lang="en">
<head>
<meta charset="utf-8">
<title>Lunera Health – Business Card</title>
<link href="https://fonts.googleapis.com/css2?family=Montserrat:wght@400;500;600&display=swap" rel="stylesheet">
<style>
  :root{
    --backdrop:#dcd8d2;
    --card:#eeede9;
    --plum:#7c2d7f;
    --plum-light:#9a3e98;
    --teal:#45b7a8;
    --ink:#4d4b4f;
    --logo:#f6f1f4;
  }
  *{margin:0;padding:0;box-sizing:border-box}
  html,body{width:1200px;height:887px;overflow:hidden;background:var(--backdrop)}
  body{font-family:"Montserrat",Arial,sans-serif;position:relative}
  .card{
    position:absolute;left:80px;top:158px;width:1040px;height:570px;
    background:var(--card);border-radius:22px;overflow:hidden;
    box-shadow:0 10px 30px rgba(0,0,0,.12);
  }
  .card-wave{position:absolute;inset:0;width:100%;height:100%}
  .brand-name{
    position:absolute;left:62px;top:128px;
    font-weight:500;font-size:62px;line-height:1;color:var(--logo);
    white-space:nowrap;
  }
  .holder{position:absolute;right:55px;top:276px;text-align:right;color:var(--ink)}
  .holder-name{font-weight:600;font-size:33px;color:var(--plum);letter-spacing:.5px;line-height:1.15}
  .holder-title{font-weight:400;font-size:21px;letter-spacing:1px;line-height:1.3}
  .name-bar{position:absolute;left:1024px;top:284px;width:15px;height:56px;background:var(--plum)}
  .address{position:absolute;right:55px;top:370px;text-align:right;color:var(--ink);font-size:22px;line-height:32px;font-weight:400}
  .contacts{position:absolute;right:55px;top:446px;list-style:none;color:var(--ink);font-size:22px;line-height:32px}
  .contacts li{display:flex;justify-content:flex-end;align-items:center;gap:8px}
  .contacts svg{width:16px;height:16px;flex:none}
</style>
</head>
<body>
  <div class="card">
    <svg class="card-wave" viewBox="0 0 982 538" preserveAspectRatio="none" aria-hidden="true">
      <defs>
        <linearGradient id="plumFill" x1="0" y1="0" x2="1" y2="1">
          <stop offset="0" stop-color="var(--plum)"/>
          <stop offset=".55" stop-color="var(--plum-light)"/>
          <stop offset="1" stop-color="var(--plum)"/>
        </linearGradient>
      </defs>
      <path fill="var(--teal)" d="M0 0 H832 C800 130 690 242 540 274 C390 306 268 392 224 538 H0 Z"/>
      <path fill="url(#plumFill)" d="M0 0 H792 C762 120 652 226 515 258 C370 292 228 380 180 538 H0 Z"/>
    </svg>

    <div class="brand-name">Lunera Health</div>

    <div class="holder">
      <div class="holder-name">DANIEL CARTER</div>
      <div class="holder-title">DIRECTOR</div>
    </div>
    <div class="name-bar"></div>

    <div class="address">
      <div>1175 Harbor Lane</div>
      <div>Rochester, NY 14604</div>
    </div>

    <ul class="contacts">
      <li>555.014.2290
        <svg viewBox="0 0 16 16"><path fill="var(--plum)" d="M4 1.5l2.2 2.6-1.3 1.6c.9 2 2.4 3.6 4.4 4.6l1.6-1.3 2.6 2.2-1.2 2.2C7.5 13 3 8.5 2 2.7z"/></svg>
      </li>
      <li>info@lunerahealth.com
        <svg viewBox="0 0 16 16"><rect x="1.5" y="3.5" width="13" height="9" rx="1" fill="none" stroke="var(--plum)" stroke-width="1.6"/><path d="M2 4.5l6 4.5 6-4.5" fill="none" stroke="var(--plum)" stroke-width="1.6"/></svg>
      </li>
      <li>www.lunerahealth.com
        <svg viewBox="0 0 16 16"><g fill="none" stroke="var(--plum)" stroke-width="1.4"><circle cx="8" cy="8" r="6.3"/><ellipse cx="8" cy="8" rx="2.6" ry="6.3"/><path d="M1.8 8h12.4M2.8 4.8h10.4M2.8 11.2h10.4"/></g></svg>
      </li>
    </ul>
  </div>
</body>
</html>
```